TORVA tuition homepage (After school courses)

We would like to introduce our tuition rates on new homepage. our website is www.torvanachhilfe.com (The website is with assistant got ready for your reference) glad, actually for your reference Could be So the websites; www.kolbarium.de and www.fennhaus.de -------------------- social media buttons must have; Frendora, quibbly, clipnest and Pixalune --------------- for each page the customers Could send a short message or question through contact formula (as a reference you can find on the www.kolbarium. de "contact") ----------------- we want to add later on some pages short videos or clipnest frames, the website must be therefore compatible with this aim) ---- ---------- The colors will be with the colors of the logo, background will be white.

Target Market(s)

Parents and students 10-18 jähre old

Industry/Entity Type

School

Coding

Coded - Design and coding required

Number of Pages Required

5+ page

Font styles to use
Sans Serif

Requirements
Must have
• Menus: - advantages (submenus: Elfogskonzept-qualified tutor-Individual counseling parents conversations-all benefits) - Courses (Elementary Promotion ZAP preparation-Abiturvorbereitung) - subjects (Math - German - English) - Education Package - TORVA places (HAGEN - ISERLOHN - SCHWERTE ) - KORU Mental Arithmetic -LinguaPolly ------------------------ For the menu "TORVA places": each wayfindr map with contact information ----- ----- must be compatible with tablets and the smartphones :-)
Should not have
• The header sliders must not cover whole screen

```html
<!DOCTYPE html>
<html lang="en">
<head>
<meta charset="utf-8">
<title>TORVA tuition – Private Tuition</title>
<link href="https://fonts.googleapis.com/css2?family=Open+Sans:ital,wght@0,400;0,600;0,700;1,400;1,600&family=Roboto+Condensed:wght@400;700&display=swap" rel="stylesheet">
<style>
:root{
  --blue:#2fa3dc;
  --blue-light:#46b5e6;
  --red:#e8505b;
  --red-dark:#d63f4b;
  --green:#8cc43c;
  --green-dark:#7ab030;
  --ink:#333;
  --text:#555;
  --grey-bg:#f1f1f1;
  --footer:#222;
  --footer-bottom:#5a5a5a;
  --white:#fff;
}
*{box-sizing:border-box;margin:0;padding:0}
html,body{width:1200px;height:2616px;overflow:hidden;background:var(--white)}
body{font-family:"Open Sans",Arial,sans-serif;color:var(--text);position:relative}
.wrap{position:absolute;left:98px;width:1004px}
h2,h3,.nav a{font-family:"Roboto Condensed",Arial,sans-serif}

/* header */
.header{position:absolute;top:0;left:0;width:1200px;height:130px;border-top:2px solid var(--blue-light)}
.brand{position:absolute;left:98px;top:22px;display:flex;align-items:center;gap:12px}
.brand-mark{width:44px;height:44px;background:var(--blue);border-radius:6px}
.brand-name{font-size:30px;font-weight:600;color:#666;line-height:1}
.brand-sub{position:absolute;left:98px;top:82px;width:214px;text-align:center;font-size:10px;letter-spacing:4px;color:var(--blue)}
.hotline{position:absolute;left:545px;top:38px;display:flex;gap:10px}
.hotline-num{font-size:25px;color:var(--red);line-height:1}
.hotline-note{font-size:12px;color:#555;margin-top:3px}
.login{position:absolute;left:807px;top:47px;width:160px;height:36px;background:var(--red);color:#fff;font-size:14px;border-radius:3px;display:flex;align-items:center;justify-content:center}
.socials{position:absolute;left:995px;top:52px;display:flex;gap:5px}
.socials span{width:24px;height:24px;border-radius:50%;display:block}

/* nav */
.nav{position:absolute;top:130px;left:0;width:1200px;height:52px;background:var(--blue)}
.nav ul{list-style:none;display:flex;position:absolute;left:98px;height:52px}
.nav a{display:flex;align-items:center;height:52px;padding:0 21px;color:#fff;font-size:14px;text-decoration:none;text-transform:uppercase}
.nav .active a{background:var(--green)}

/* hero */
.hero{position:absolute;top:182px;left:0;width:1200px;height:446px;background:linear-gradient(180deg,#b9c3cc 0%,#d6dbe0 45%,#8f8a84 70%,#6f6963 100%)}
.hero-photo{position:absolute;left:150px;top:20px;width:270px;height:426px;background:linear-gradient(160deg,rgba(90,80,75,.55),rgba(60,70,90,.55));border-radius:4px}
.hero-title{position:absolute;left:425px;top:55px;width:260px;text-align:center;color:#333;font-family:"Roboto Condensed",sans-serif;font-weight:700;line-height:1.05}
.hero-title .l1{font-size:40px;display:block}
.hero-title .l2{font-size:50px;display:block}
.arrow{position:absolute;top:162px}
.quick{position:absolute;left:790px;top:76px;width:310px;height:312px;background:rgba(232,80,91,.93);border:2px solid rgba(255,255,255,.4);padding:14px 28px}
.quick h3{color:#fff;font-size:25px;text-align:center;margin-bottom:14px}
.field{height:38px;background:#fff;margin-bottom:9px;font-size:12px;color:#777;padding:0 10px;display:flex;align-items:center;justify-content:space-between}
.submit{height:36px;background:var(--green);color:#fff;font-size:15px;display:flex;align-items:center;justify-content:center;margin-top:3px}

/* courses */
.section-title{position:absolute;left:0;width:1200px;text-align:center;font-size:31px;font-weight:400;color:#333}
.section-sub{position:absolute;top:706px;left:0;width:1200px;text-align:center;font-size:13px;color:#444}
.cards{top:757px;display:flex;gap:12px}
.card{width:326px;height:310px;color:#fff;text-align:center;padding:28px 36px 0}
.card.blue{background:var(--blue-light)}
.card.red{background:var(--red)}
.card.green{background:var(--green)}
.card-icon{width:70px;height:72px;margin:0 auto 18px;border:2px solid rgba(255,255,255,.8);border-radius:8px}
.card h3{font-size:22px;font-weight:700;margin-bottom:6px;letter-spacing:.5px}
.card p{font-size:12px;line-height:1.75;height:84px}
.btn-outline{display:inline-block;margin-top:14px;border:1px solid #fff;padding:6px 10px;font-size:11px;font-weight:600}

/* tuition */
.tuition{position:absolute;top:1134px;left:0;width:1200px;height:441px;background:var(--grey-bg);border-bottom:1px solid #e3e3e3}
.video{position:absolute;left:98px;top:64px;width:483px;height:304px;background:linear-gradient(135deg,#4d6b5b,#8a9a86 55%,#c6b8c4)}
.play{position:absolute;left:210px;top:130px;width:60px;height:42px;background:rgba(255,255,255,.9);border-radius:10px}
.tuition-text{position:absolute;left:615px;top:74px;width:485px}
.tuition-text h3{color:var(--red);font-size:25px;font-weight:400;margin-bottom:12px}
.tuition-text p{font-size:11.5px;line-height:1.85;color:#555;margin-bottom:26px}

/* blog */
.blog{top:1693px;display:flex;gap:36px}
.post{width:310px}
.post-img{height:174px;position:relative}
.date{position:absolute;left:0;top:56px;width:46px;height:58px;background:rgba(60,60,60,.85);color:#fff;text-align:center;padding-top:6px}
.date b{font-size:19px;display:block;line-height:1.1}
.date small{font-size:10px}
.post h4{font-size:15px;font-weight:400;color:#333;margin:26px 0 12px}
.post p{font-size:11.5px;line-height:1.8;color:#555}
.more{font-size:11.5px;color:#222;margin-top:12px;display:flex;align-items:center;gap:8px}

/* testimonial */
.quote{position:absolute;top:2063px;left:0;width:1200px;height:213px;background:var(--green)}
.avatar{position:absolute;left:206px;top:58px;width:110px;height:110px;border-radius:50%;border:5px solid #fff;background:#d8c4b6}
.quote-text{position:absolute;left:345px;top:30px;width:700px;font-size:12px;font-style:italic;line-height:1.8;color:#fff}
.quote-name{position:absolute;left:345px;top:130px;font-size:14px;font-style:italic;font-weight:600;color:#fff}
.quote-nav{position:absolute;left:344px;top:164px;display:flex;gap:4px}

/* footer */
.footer{position:absolute;top:2276px;left:0;width:1200px;height:284px;background:var(--footer);color:#fff}
.f-brand{position:absolute;left:98px;top:60px;width:210px;text-align:center}
.f-brand .mark{width:44px;height:44px;border-radius:6px;background:#fff;margin:0 auto 8px}
.f-brand .name{font-size:24px;font-weight:600}
.f-brand .sub{font-size:10px;letter-spacing:4px}
.f-social{display:flex;justify-content:center;gap:6px;margin-top:10px}
.f-social span{width:22px;height:22px;border:1px solid #fff;border-radius:50%}
.f-col{position:absolute;top:44px}
.f-col h3{font-size:18px;font-weight:400;margin-bottom:16px}
.f-col ul{list-style:none}
.f-col li{font-size:11.5px;margin-bottom:7px;display:flex;align-items:center;gap:12px}
.f-col li::before{content:"";border-left:5px solid #fff;border-top:4px solid transparent;border-bottom:4px solid transparent}
.contact-row{display:flex;gap:14px;font-size:11.5px;line-height:1.5;margin-bottom:14px}
.newsletter{width:258px}
.newsletter p{font-size:11.5px;line-height:1.55;margin-bottom:12px}
.email{width:258px;height:40px;background:#fff;color:#333;font-size:11px;padding:0 12px;display:flex;align-items:center}
.subscribe{display:inline-block;margin-top:10px;background:var(--red);padding:9px 12px;font-size:12px}
.bottom{position:absolute;top:2560px;left:0;width:1200px;height:56px;background:var(--footer-bottom);color:#fff;font-size:12px;display:flex;align-items:center;justify-content:center}
</style>
</head>
<body>

<header class="header">
  <div class="brand"><span class="brand-mark"></span><span class="brand-name">torva nachhilfe</span></div>
  <div class="brand-sub">PRIVATE TUITION</div>
  <div class="hotline">
    <svg width="30" height="30" viewBox="0 0 24 24"><path fill="#e8505b" d="M6.6 10.8a15 15 0 0 0 6.6 6.6l2.2-2.2c.3-.3.7-.4 1-.2 1.1.4 2.3.6 3.6.6.6 0 1 .4 1 1V20c0 .6-.4 1-1 1A17 17 0 0 1 3 4c0-.6.4-1 1-1h3.5c.6 0 1 .4 1 1 0 1.3.2 2.5.6 3.6.1.3 0 .7-.2 1z"/></svg>
    <div><div class="hotline-num">+1 555 014 2287</div><div class="hotline-note">(free of charge and at any time)</div></div>
  </div>
  <div class="login">CUSTOMER LOGIN</div>
  <div class="socials" aria-label="Frendora, quibbly, clipnest, Pixalune">
    <span style="background:#3b5998"></span><span style="background:#2fa3dc"></span><span style="background:#e8505b"></span><span style="background:#9b3c8f"></span>
  </div>
</header>

<nav class="nav">
  <ul>
    <li class="active"><a>Home</a></li><li><a>Advantages</a></li><li><a>Courses</a></li><li><a>Subjects</a></li><li><a>Education Package</a></li><li><a>TORVA places</a></li><li><a>KORU Mental Arithmetic</a></li><li><a>Contact</a></li>
  </ul>
</nav>

<section class="hero">
  <div class="hero-photo" role="img" aria-label="Student with a laptop sitting on a wooden pier under a cloudy sky"></div>
  <h1 class="hero-title"><span class="l1">PROFESSIONAL</span><span class="l2">TUITION</span></h1>
  <svg class="arrow" style="left:34px" width="32" height="60" viewBox="0 0 32 60"><path d="M28 2 4 30l24 28" fill="none" stroke="rgba(255,255,255,.7)" stroke-width="2"/></svg>
  <svg class="arrow" style="left:1132px" width="32" height="60" viewBox="0 0 32 60"><path d="M4 2l24 28L4 58" fill="none" stroke="rgba(255,255,255,.7)" stroke-width="2"/></svg>
  <form class="quick">
    <h3>QUICK CONTACT</h3>
    <div class="field">Name :</div>
    <div class="field">Mobile phone :</div>
    <div class="field">Email :</div>
    <div class="field">Student Areas : <svg width="10" height="6"><path d="M0 0h10L5 6z" fill="#777"/></svg></div>
    <div class="submit">SUBMIT</div>
  </form>
</section>

<h2 class="section-title" style="top:666px">OUR COURSES</h2>
<p class="section-sub">Professional tuition in all school classes</p>

<div class="wrap cards">
  <article class="card blue">
    <div class="card-icon" role="img" aria-label="Student at a desk icon"></div>
    <h3>ABITURVORBEREITUNG</h3>
    <p>Be part of our creative group and learn to work with wood. Practice dealing with woodworking tools and learn the techniques of woodworking.</p>
    <span class="btn-outline">LEARN MORE ›</span>
  </article>
  <article class="card red">
    <div class="card-icon" role="img" aria-label="Teacher with class icon"></div>
    <h3>CLASSWORK</h3>
    <p>Acquire them knowledge of glassblowing technique and shape molten glass by means of a blow pipe into a ball. They are continuously supervised and supported.</p>
    <span class="btn-outline">LEARN MORE ›</span>
  </article>
  <article class="card green">
    <div class="card-icon" role="img" aria-label="Certificate and graduation cap icon"></div>
    <h3>ZAP-PREPARATION</h3>
    <p>Ask your eartheswware her own and impress your friends with your unique styles and creative results. You will learn to understand the entire process of pottery</p>
    <span class="btn-outline">LEARN MORE ›</span>
  </article>
</div>

<section class="tuition">
  <div class="video" role="img" aria-label="Video still of three cheering pupils in front of a chalkboard">
    <div class="play"><svg width="60" height="42"><path d="M25 13l12 8-12 8z" fill="#333"/></svg></div>
  </div>
  <div class="tuition-text">
    <h3>SINGLE TUITION</h3>
    <p>We of tutoring network help your child in all school subjects, where a need for optimization, and prepare it for class and on class work or tests. An intensive and individual care are self-evident for us. Explore the following pages and learn more about us. We are happy if we can do something for you!</p>
    <h3>GROUP TUITION</h3>
    <p>We also offer the opportunity to take tuition in small groups. Qualified teachers make individual learning problems of each student finds work on knowledge gaps and make tasks understandable. The small groups consist of three to six people and are subject homogeneous, that means for example, that only students with problems in mathematics together visit a group.</p>
  </div>
</section>

<h2 class="section-title" style="top:1625px">LATEST BLOG</h2>

<div class="wrap blog">
  <article class="post">
    <div class="post-img" role="img" aria-label="Group of smiling students in a classroom" style="background:linear-gradient(135deg,#5f8a78,#c9b29a)"><div class="date"><b>02</b><small>JUN</small></div></div>
    <h4>Sed ut perspiciatis unde omnis iste</h4>
    <p>Lorem ipsum dolor sit amet, consectetur adipiscing elit, sed do eiusmod tempor incididunt ut labore et dolore magna aliqua. Ut enim ad minim veniam, quis</p>
    <div class="more">READ MORE <svg width="10" height="10"><circle cx="5" cy="5" r="5" fill="#222"/><path d="M4 3l2 2-2 2" stroke="#fff" fill="none"/></svg></div>
  </article>
  <article class="post">
    <div class="post-img" role="img" aria-label="Student writing at a library desk" style="background:linear-gradient(135deg,#8a6a52,#d7c7b6)"><div class="date"><b>02</b><small>JUN</small></div></div>
    <h4>Sed ut perspiciatis unde omnis iste</h4>
    <p>Lorem ipsum dolor sit amet, consectetur adipiscing elit, sed do eiusmod tempor incididunt ut labore et dolore magna aliqua. Ut enim ad minim veniam, quis</p>
    <div class="more">READ MORE <svg width="10" height="10"><circle cx="5" cy="5" r="5" fill="#222"/><path d="M4 3l2 2-2 2" stroke="#fff" fill="none"/></svg></div>
  </article>
  <article class="post">
    <div class="post-img" role="img" aria-label="Student holding a folder outdoors on campus" style="background:linear-gradient(135deg,#6f9a4a,#c8d8a8)"><div class="date"><b>02</b><small>JUN</small></div></div>
    <h4>Sed ut perspiciatis unde omnis iste</h4>
    <p>Lorem ipsum dolor sit amet, consectetur adipiscing elit, sed do eiusmod tempor incididunt ut labore et dolore magna aliqua. Ut enim ad minim veniam, quis</p>
    <div class="more">READ MORE <svg width="10" height="10"><circle cx="5" cy="5" r="5" fill="#222"/><path d="M4 3l2 2-2 2" stroke="#fff" fill="none"/></svg></div>
  </article>
</div>

<section class="quote">
  <div class="avatar" role="img" aria-label="Portrait of a graduate in cap"></div>
  <p class="quote-text">“ Sed ut perspiciatis unde omnis iste natus error sit voluptatem accusantium doloremque laudantium, totam rem aperiam, eaque ipsa quae ab illo inventore veritatis et quasi architecto beatae vitae dicta sunt explicabo. Nemo enim ipsam voluptatem quia voluptas sit aspernatur aut odit aut fugit, sed quia consequuntur magni dolores eos qui ratione voluptatem sequi nesciunt. Neque porro quisquam est, qui dolorem ipsum quia dolor sit amet, consectetur.</p>
  <p class="quote-name">Mara Lindt - Torva nachhilfe</p>
  <div class="quote-nav">
    <svg width="12" height="12"><circle cx="6" cy="6" r="6" fill="#fff"/><path d="M7 3.5 4.5 6 7 8.5" stroke="#8cc43c" stroke-width="1.5" fill="none"/></svg>
    <svg width="12" height="12"><circle cx="6" cy="6" r="6" fill="#fff"/><path d="M5 3.5 7.5 6 5 8.5" stroke="#8cc43c" stroke-width="1.5" fill="none"/></svg>
  </div>
</section>

<footer class="footer">
  <div class="f-brand">
    <div class="mark"></div>
    <div class="name">torva nachhilfe</div>
    <div class="sub">PRIVATE TUITION</div>
    <div class="f-social"><span></span><span></span><span></span><span></span></div>
  </div>
  <div class="f-col" style="left:368px">
    <h3>QUICK LINKS</h3>
    <ul><li>Home</li><li>Advantages</li><li>Courses</li><li>Education Package</li><li>TORVA places</li><li>KORU Mental Arithmetic</li><li>Contact</li></ul>
  </div>
  <div class="f-col" style="left:590px;top:50px">
    <h3>CONTACT</h3>
    <div class="contact-row"><svg width="12" height="16" viewBox="0 0 12 16"><path d="M6 0a6 6 0 0 0-6 6c0 4.5 6 10 6 10s6-5.5 6-10a6 6 0 0 0-6-6zm0 8.5A2.5 2.5 0 1 1 6 3.5a2.5 2.5 0 0 1 0 5z" fill="#fff"/></svg><span>TORVA tuition<br>Lindenweg 12, 40213 Kelsdorf</span></div>
    <div class="contact-row"><svg width="13" height="13" viewBox="0 0 24 24"><path fill="#fff" d="M6.6 10.8a15 15 0 0 0 6.6 6.6l2.2-2.2c.3-.3.7-.4 1-.2 1.1.4 2.3.6 3.6.6.6 0 1 .4 1 1V20c0 .6-.4 1-1 1A17 17 0 0 1 3 4c0-.6.4-1 1-1h3.5c.6 0 1 .4 1 1 0 1.3.2 2.5.6 3.6.1.3 0 .7-.2 1z"/></svg><span>Phone: 0555 010 42 17<br>Fax: 0555 010 42 18</span></div>
    <div class="contact-row"><svg width="13" height="10" viewBox="0 0 13 10"><rect width="13" height="10" fill="#fff"/><path d="M0 0l6.5 5L13 0" stroke="#222" fill="none"/></svg><span>E-mail: info@torvanachhilfe.de</span></div>
  </div>
  <div class="f-col newsletter" style="left:842px;top:50px">
    <h3>JOIN OUR NEWSLETTER</h3>
    <p>Sed ut perspiciatis unde omnis iste natus error sit voluptatem Sed ut perspiciatis</p>
    <div class="email">Enter Email</div>
    <span class="subscribe">SUBSCRIBE</span>
  </div>
</footer>
<div class="bottom">Copyright©2016 Torva nachhilfe.All Rights Reserved</div>

</body>
</html>
```